Business Card Design

Need a hot business card in wine colors something cool and mod please feel free to be , FUNKY and free with this .

Industry/Entity Type

Business

Contact Information for Business Card

LUMERA HAIR DESIGN 3182 w 9th st scottsdale az 85619 Custom modern hair design and custom color by MARCUS OBRIDGE 602-4168203 cell salon 480 -712-6084 email marcusobridge@quillpost.com hours wed thru sat 7am to 6pm.

Font styles to use
Other font styles liked:
• something fun and mod.

Colors
a54599
6b449b
1b1b1b
606060

Requirements
Must have
• Apointment reminder on flip side of card.
Should not have
• Nothing boring.

```html
<!DOCTYPE html>
<html lang="en">
<head>
<meta charset="utf-8">
<title>Lumera Hair Design – Appointment Card</title>
<link rel="stylesheet" href="https://fonts.googleapis.com/css2?family=Caudex:ital,wght@0,400;1,400&family=Macondo&display=swap">
<style>
  :root {
    --card-bg: #ffffff;
    --brand-violet: #a644e0;
    --ink: #111111;
  }
  html, body {
    margin: 0;
    padding: 0;
    width: 1200px;
    height: 702px;
    overflow: hidden;
    background: var(--card-bg);
  }
  .appointment-card {
    position: relative;
    width: 1200px;
    height: 702px;
    background: var(--card-bg);
    color: var(--ink);
    font-family: "Caudex", "Palatino Linotype", serif;
  }
  .brand-name {
    position: absolute;
    left: 0;
    width: 100%;
    top: 30px;
    text-align: center;
    font-size: 104px;
    line-height: 1;
    color: var(--brand-violet);
    letter-spacing: 8px;
  }
  .brand-tagline {
    position: absolute;
    left: 0;
    width: 100%;
    top: 156px;
    text-align: center;
    font-style: italic;
    font-size: 50px;
    line-height: 1;
    letter-spacing: -1px;
  }
  .card-title {
    position: absolute;
    left: 0;
    width: 100%;
    top: 214px;
    text-align: center;
    font-size: 48px;
    line-height: 1;
    color: var(--brand-violet);
  }
  .field {
    position: absolute;
    display: flex;
    align-items: baseline;
    font-size: 48px;
    line-height: 1;
  }
  .field-line {
    display: inline-block;
    flex: 1;
    border-bottom: 3px solid var(--ink);
    margin-left: 2px;
    transform: translateY(4px);
  }
  .field--name { left: 229px; width: 790px; top: 295px; }
  .field--date { left: 226px; width: 794px; top: 391px; }
  .field--time { left: 221px; width: 804px; top: 487px; }
  .services-line {
    position: absolute;
    left: 0;
    width: 100%;
    top: 586px;
    text-align: center;
    font-family: "Macondo", "Papyrus", cursive;
    font-size: 54px;
    line-height: 1;
  }
</style>
</head>
<body>
  <main class="appointment-card">
    <div class="brand-name">Lumera</div>
    <div class="brand-tagline">HAIR DESIGN</div>
    <div class="card-title">Appointment Card</div>

    <div class="field field--name"><span class="field-label">Name:</span><span class="field-line"></span></div>
    <div class="field field--date"><span class="field-label">Date:</span><span class="field-line"></span></div>
    <div class="field field--time"><span class="field-label">Time:</span><span class="field-line"></span></div>

    <div class="services-line">Custom modern hair designs and color</div>
  </main>
</body>
</html>
```